Ductless Mini Split Business Website

Amber Kite Services is looking to design an eye catching educational website about installing Ductless mini splits.

Similar to this company.
https://www.cedarcoolair.com/

```html
<!DOCTYPE html>
<html lang="en">
<head>
<meta charset="utf-8">
<title>Amber Kite Ductless Experts</title>
<link href="https://fonts.googleapis.com/css2?family=Poppins:ital,wght@0,400;0,500;0,600;1,400&family=Rubik:wght@500;600;700&display=swap" rel="stylesheet">
<style>
:root{
  --yellow:#f8c300;
  --yellow-deep:#eeb400;
  --ink:#1d1d1d;
  --text:#555;
  --muted:#8a8a8a;
  --light:#f3f3f3;
  --footer:#151515;
  --white:#fff;
}
*{box-sizing:border-box;margin:0;padding:0}
html,body{width:1200px;height:4797px;overflow:hidden}
body{position:relative;background:var(--white);font-family:"Poppins",sans-serif;color:var(--text)}
.abs{position:absolute}
.head-font{font-family:"Rubik",sans-serif}
.btn{position:absolute;background:var(--yellow);color:var(--white);font-family:"Rubik",sans-serif;font-weight:500;letter-spacing:1px;font-size:17px;display:flex;align-items:center;justify-content:center;border-radius:4px;box-shadow:0 4px 10px rgba(0,0,0,.12)}
.photo{position:absolute}

/* header */
.site-header{left:0;top:0;width:1200px;height:82px;background:var(--white);box-shadow:0 2px 8px rgba(0,0,0,.06);z-index:3}
.brand{left:76px;top:16px;display:flex;align-items:center;gap:10px}
.brand-mark{width:22px;height:22px;background:var(--yellow);border-radius:4px}
.brand-name{font-family:"Rubik",sans-serif;font-weight:600;font-size:20px;color:var(--ink);line-height:1}
.brand-sub{left:82px;top:56px;font-family:"Rubik",sans-serif;font-weight:600;font-size:13px;color:var(--ink);letter-spacing:.5px}
.main-nav{left:336px;top:0;height:82px;display:flex;gap:24px;align-items:center;font-size:14px;color:#333}
.main-nav a{text-decoration:none;color:inherit;height:82px;display:flex;align-items:center}
.main-nav a.active{color:var(--yellow);border-bottom:3px solid var(--yellow)}
.call-box{left:960px;top:0;width:240px;height:82px;background:var(--yellow);color:var(--white)}
.call-box svg{position:absolute;left:34px;top:24px}
.call-label{position:absolute;left:84px;top:20px;font-size:14px}
.call-number{position:absolute;left:84px;top:42px;font-family:"Rubik",sans-serif;font-weight:600;font-size:19px;letter-spacing:.5px}

/* hero */
.hero{left:0;top:82px;width:1200px;height:594px;background:linear-gradient(90deg,#8c9095 0%,#a9adb1 45%,#c7c8c9 70%,#b3b4b6 100%)}
.hero-title{left:78px;top:255px;font-family:"Rubik",sans-serif;font-weight:700;font-size:58px;line-height:58px;color:#2a2414}
.hero-sub{left:80px;top:382px;font-size:18px;color:#222}
.slider-arrow{width:46px;height:46px;border:2px solid rgba(255,255,255,.7);border-radius:50%;top:297px}

/* feature grid */
.tile{position:absolute;width:300px;height:290px}
.tile.yellow{background:var(--yellow);color:var(--ink);display:flex;flex-direction:column;align-items:center;justify-content:center;text-align:center;font-family:"Rubik",sans-serif;font-weight:500;font-size:20px;line-height:26px}
.tile.yellow svg{margin-bottom:18px}
.welcome{left:600px;top:596px;width:600px;height:620px;background:#f1f1f1}
.welcome-kicker{left:600px;top:628px;width:568px;text-align:center;font-size:18px;color:#333}
.welcome-title{left:600px;top:660px;width:568px;text-align:center;font-family:"Rubik",sans-serif;font-weight:600;font-size:38px;line-height:46px;color:var(--ink)}
.welcome-text{left:680px;top:766px;width:408px;text-align:center;font-size:14px;line-height:27px;color:var(--muted)}

/* services */
.kicker{position:absolute;width:1200px;text-align:center;font-size:18px;color:#333}
.section-title{position:absolute;width:1200px;text-align:center;font-family:"Rubik",sans-serif;font-weight:500;font-size:38px;color:var(--ink);letter-spacing:.5px}
.service-card{position:absolute;width:291px;height:354px;background:var(--white);box-shadow:0 2px 12px rgba(0,0,0,.1)}
.service-card .photo{left:7px;top:7px;width:277px;height:238px}
.service-card .plus{position:absolute;right:20px;top:224px;width:44px;height:44px;border-radius:50%;background:var(--yellow);color:var(--ink);font-size:26px;display:flex;align-items:center;justify-content:center;font-weight:400}
.service-card h3{position:absolute;left:22px;top:284px;font-family:"Rubik",sans-serif;font-weight:500;font-size:17px;line-height:26px;color:var(--ink);letter-spacing:.5px}

/* testimonials */
.testimonial-box{left:743px;top:2361px;width:364px;height:470px;background:linear-gradient(160deg,var(--yellow) 0%,#f0b800 100%);color:var(--white);text-align:center}
.testimonial-box .kicker-s{position:absolute;top:58px;width:100%;font-size:17px}
.testimonial-box h2{position:absolute;top:86px;width:100%;font-family:"Rubik",sans-serif;font-weight:500;font-size:38px;letter-spacing:1px}
.quote-badge{position:absolute;left:146px;top:150px;width:70px;height:70px;border-radius:50%;background:var(--white)}
.testimonial-box p{position:absolute;left:40px;top:244px;width:284px;font-style:italic;font-size:15px;line-height:27px}
.testimonial-box .client{position:absolute;top:412px;width:100%;font-family:"Rubik",sans-serif;font-weight:500;font-size:17px;color:var(--ink);letter-spacing:.5px}

/* stand behind */
.intro-sub{position:absolute;width:1200px;text-align:center;font-size:16px;color:#666}
.help-card{position:absolute;left:617px;width:467px;height:140px;background:var(--white);box-shadow:0 3px 14px rgba(0,0,0,.1)}
.help-card .photo{left:12px;top:12px;width:124px;height:114px}
.help-card h3{position:absolute;left:160px;top:28px;font-family:"Rubik",sans-serif;font-weight:500;font-size:20px;color:var(--ink);letter-spacing:.5px}
.help-card p{position:absolute;left:163px;top:60px;font-size:14px;color:var(--muted)}
.help-card .btn{right:0;top:88px;height:44px;font-size:17px;border-radius:0}

/* contact */
.contact-bg{left:0;top:3720px;width:1200px;height:672px;background:linear-gradient(180deg,#ffffff 0%,#f2f2f2 30%,#ececec 100%);clip-path:polygon(0 25%,100% 0,100% 100%,0 100%)}
.field{position:absolute;background:var(--white);border:1px solid #e2e2e2;font-size:14px;color:#777;padding:16px 18px}

/* call band + footer */
.call-band{left:0;top:4391px;width:1200px;height:105px;background:linear-gradient(90deg,var(--yellow-deep),var(--yellow))}
.call-band .line{position:absolute;left:182px;top:34px;font-family:"Rubik",sans-serif;font-weight:500;font-size:29px;color:var(--white);letter-spacing:.5px}
.call-band .pill{position:absolute;left:750px;top:25px;width:267px;height:56px;border:2px solid var(--white);border-radius:6px;background:rgba(255,255,255,.12)}
.call-band .pill span{position:absolute;left:66px;top:11px;font-family:"Rubik",sans-serif;font-weight:600;font-size:26px;color:var(--ink)}
.site-footer{left:0;top:4496px;width:1200px;height:301px;background:var(--footer);color:#bbb}
.site-footer h4{position:absolute;font-family:"Rubik",sans-serif;font-weight:500;font-size:17px;color:var(--white);letter-spacing:.5px}
.footer-links{position:absolute;left:680px;top:82px;list-style:none;font-size:14px;line-height:27px}
.footer-links li::before{content:"";display:inline-block;width:6px;height:6px;border-radius:50%;background:var(--yellow);margin-right:18px;vertical-align:middle}
.footer-contact{position:absolute;left:890px;font-size:14px;line-height:27px}
.social{position:absolute;top:4675px;width:44px;height:44px;border-radius:50%;background:#3a3a3a;border:2px solid var(--yellow)}
</style>
</head>
<body>

<header class="abs site-header">
  <div class="abs brand"><span class="brand-mark"></span><span class="brand-name">Amber Kite</span></div>
  <div class="abs brand-sub">DUCTLESS EXPERTS</div>
  <nav class="abs main-nav">
    <a class="active" href="#">HOME</a><a href="#">ABOUT US</a><a href="#">SERVICES</a><a href="#">FAQ's</a><a href="#">FINANCING</a><a href="#">REVIEWS</a><a href="#">CONTACT US</a>
  </nav>
  <div class="abs call-box">
    <svg width="34" height="34" viewBox="0 0 24 24" fill="none" stroke="#fff" stroke-width="2"><path d="M5 3h4l2 5-2.5 1.5a11 11 0 0 0 6 6L16 13l5 2v4a2 2 0 0 1-2 2A16 16 0 0 1 3 5a2 2 0 0 1 2-2z"/></svg>
    <div class="call-label">Call Us Today :</div>
    <div class="call-number">123 456 7890</div>
  </div>
</header>

<section class="abs hero" role="img" aria-label="Woman on a sofa cooling a living room with a wall-mounted ductless unit"></section>
<div class="abs slider-arrow" style="left:14px"></div>
<div class="abs slider-arrow" style="left:1138px"></div>
<h1 class="abs hero-title">Amber Kite<br>Does It Better</h1>
<p class="abs hero-sub">Let Ductless Heroes Show You How</p>
<a class="btn" style="left:76px;top:416px;width:252px;height:52px">GET STARTED WITH US</a>

<section>
  <div class="tile yellow" style="left:0;top:636px">
    <svg width="64" height="64" viewBox="0 0 64 64" fill="none" stroke="#fff" stroke-width="2.5"><circle cx="22" cy="18" r="10"/><ellipse cx="26" cy="46" rx="14" ry="5"/><ellipse cx="26" cy="38" rx="14" ry="5"/><path d="M48 56V26m-7 7 7-7 7 7"/></svg>
    0% Financing<br>for 60 months
  </div>
  <div class="photo" style="left:300px;top:596px;width:300px;height:327px;background:linear-gradient(160deg,#eeeeee,#b9bcc0 60%,#8a6f70)" role="img" aria-label="Technician servicing a ceiling cassette unit"></div>
  <div class="photo" style="left:0;top:923px;width:300px;height:293px;background:linear-gradient(170deg,#f1f1f1,#c7c4c2 50%,#6a5b52)" role="img" aria-label="Installer mounting an indoor ductless head"></div>
  <div class="tile yellow" style="left:300px;top:923px;height:293px">
    <svg width="64" height="64" viewBox="0 0 64 64" fill="none" stroke="#fff" stroke-width="2.5"><rect x="6" y="8" width="52" height="40" rx="3"/><circle cx="32" cy="28" r="11"/><path d="M32 21v14M28 25h6a3 3 0 0 1 0 6h-6"/><path d="M20 56h24"/></svg>
    365 Day, Money<br>Back Guarantee
  </div>
  <div class="abs welcome"></div>
  <div class="abs welcome-kicker">Welcome To</div>
  <h2 class="abs welcome-title">AMBER KITE DUCTLESS<br>EXPERTS</h2>
  <p class="abs welcome-text">Lorem Ipsum is simply dummy text of the printing and typesetting industry. Lorem Ipsum has been the industry's standard dummy text ever since the 1500s, when an unknown printer took a galley of type and scrambled it to make a type.</p>
  <a class="btn" style="left:806px;top:918px;width:158px;height:50px">LEARN MORE</a>
  <div class="photo" style="left:670px;top:942px;width:426px;height:274px;background:linear-gradient(180deg,rgba(241,241,241,0),#d6dbe2 50%,#b9c2cf)" role="img" aria-label="Technician installing a wall unit"></div>
</section>

<section>
  <div class="kicker" style="top:1278px">Our Services</div>
  <h2 class="section-title" style="top:1312px">HOW CAN WE HELP YOU ?</h2>

  <article class="service-card" style="left:130px;top:1401px"><div class="photo" style="background:linear-gradient(135deg,#cfd6dc,#9aa6b0)" role="img" aria-label="Technician holding a unit filter"></div><span class="plus">+</span><h3>BASEBOARD HEAT<br>REPLACEMENT</h3></article>
  <article class="service-card" style="left:455px;top:1401px"><div class="photo" style="background:linear-gradient(135deg,#f2f2f2,#c9c9c9)" role="img" aria-label="Woman using a remote toward a wall unit"></div><span class="plus">+</span><h3>DUCTLESS FOR ADDITIONS<br>&amp; REMODELS</h3></article>
  <article class="service-card" style="left:777px;top:1401px"><div class="photo" style="background:linear-gradient(135deg,#d9dce0,#8795a6)" role="img" aria-label="Smiling technician giving a thumbs up"></div><span class="plus">+</span><h3>DUCTLESS HEAT<br>PUMP FAQ</h3></article>

  <article class="service-card" style="left:130px;top:1792px"><div class="photo" style="background:linear-gradient(135deg,#e8e6e3,#8d98aa)" role="img" aria-label="Installer fitting a unit on a brick wall"></div><span class="plus">+</span><h3>DUCTLESS<br>INSTALLATION</h3></article>
  <article class="service-card" style="left:455px;top:1792px"><div class="photo" style="background:linear-gradient(135deg,#f0efed,#c6c0b8)" role="img" aria-label="Woman cleaning a wall unit"></div><span class="plus">+</span><h3>DUCTLESS<br>MAINTENANCE</h3></article>
  <article class="service-card" style="left:777px;top:1792px"><div class="photo" style="background:linear-gradient(135deg,#9a6f55,#6f7d92)" role="img" aria-label="Repair technician with an outdoor unit"></div><span class="plus">+</span><h3>DUCTLESS<br>REPAIRS</h3></article>

  <a class="btn" style="left:490px;top:2180px;width:220px;height:50px">VIEW ALL SERVICES</a>
</section>

<section>
  <div class="photo" style="left:0;top:2291px;width:1200px;height:678px;background:linear-gradient(100deg,#6f6a62 0%,#a8a49c 40%,#d7d6d3 75%,#e3e0dc 100%)" role="img" aria-label="Couple relaxing on a sofa with a tablet"></div>
  <div class="abs testimonial-box">
    <div class="kicker-s">What Our Client Say</div>
    <h2>TESTIMONIALS</h2>
    <div class="quote-badge"><svg width="70" height="70" viewBox="0 0 70 70"><text x="35" y="52" text-anchor="middle" font-family="Rubik,sans-serif" font-size="48" font-weight="700" fill="#1d1d1d">&ldquo;</text></svg></div>
    <p>" Lorem Ipsum is simply dummy text of the printing and typesetting industry. Lorem Ipsum has been the industry's standard dummy text ever since the "</p>
    <div class="client">CLIENT NAME</div>
  </div>
</section>

<section>
  <h2 class="section-title" style="top:3030px;line-height:48px">WE STAND BEHIND OUR<br>DUCTLESS SERVICES</h2>
  <p class="intro-sub" style="top:3138px">See Other Ways We Can Help with Your Ductless Systems</p>
  <div class="photo" style="left:84px;top:3241px;width:456px;height:457px;background:radial-gradient(ellipse at 50% 45%,#d8dfe6 0%,#eef0f2 55%,#fff 75%)" role="img" aria-label="Technician reviewing paperwork with a homeowner"></div>

  <article class="help-card" style="top:3214px"><div class="photo" style="background:linear-gradient(135deg,#dfe3e6,#7b8ca0)" role="img" aria-label="Couple reading together"></div><h3>GET SOME ANSWERS</h3><p>Lorem Ipsum is simply dummy text.</p><a class="btn" style="width:180px">DUCTLESS FAQ</a></article>
  <article class="help-card" style="top:3387px"><div class="photo" style="background:linear-gradient(135deg,#f2f2f2,#a59a86)" role="img" aria-label="Stacks of coins"></div><h3>GET FINANCE OPTIONS</h3><p>Lorem Ipsum is simply dummy text.</p><a class="btn" style="width:154px">FINANCING</a></article>
  <article class="help-card" style="top:3558px"><div class="photo" style="background:linear-gradient(135deg,#eceae6,#9aa0a8)" role="img" aria-label="Woman relaxing under a wall unit"></div><h3>STAY UP TO DATE</h3><p>Lorem Ipsum is simply dummy text.</p><a class="btn" style="width:154px">OUR BLOG</a></article>
</section>

<section>
  <div class="abs contact-bg"></div>
  <div class="photo" style="left:84px;top:3726px;width:289px;height:224px;background:radial-gradient(circle at 45% 50%,#f8c300 0%,#f8c300 30%,rgba(248,195,0,0) 62%)" role="img" aria-label="Cartoon mascot character holding a wrench"></div>
  <h2 class="section-title" style="top:3922px">CONTACT US</h2>
  <p class="intro-sub" style="top:3976px">Fill Out the Form Below or Call Amber Kite Services at &nbsp;(123) 456 7890</p>
  <div class="field" style="left:281px;top:4033px;width:312px;height:51px">Name *</div>
  <div class="field" style="left:605px;top:4033px;width:312px;height:51px">Email *</div>
  <div class="field" style="left:281px;top:4095px;width:312px;height:51px">Services *</div>
  <div class="field" style="left:605px;top:4095px;width:312px;height:51px">Phone *</div>
  <div class="field" style="left:281px;top:4156px;width:636px;height:103px">Message *</div>
  <a class="btn" style="left:537px;top:4274px;width:126px;height:50px">SUBMIT</a>
</section>

<section class="abs call-band">
  <div class="line">If you Have any Question For Call Us :</div>
  <div class="pill">
    <svg style="position:absolute;left:18px;top:12px" width="30" height="30" viewBox="0 0 24 24" fill="none" stroke="#fff" stroke-width="2"><path d="M5 3h4l2 5-2.5 1.5a11 11 0 0 0 6 6L16 13l5 2v4a2 2 0 0 1-2 2A16 16 0 0 1 3 5a2 2 0 0 1 2-2z"/></svg>
    <span>123 456 7890</span>
  </div>
</section>

<footer class="abs site-footer">
  <div class="abs" style="left:76px;top:38px;display:flex;align-items:center;gap:10px"><span class="brand-mark"></span><span class="brand-name" style="color:var(--white)">Amber Kite</span></div>
  <div class="abs" style="left:78px;top:76px;font-family:Rubik,sans-serif;font-weight:600;font-size:13px;color:var(--yellow);letter-spacing:.5px">DUCTLESS EXPERTS</div>
  <p class="abs" style="left:78px;top:104px;width:380px;font-size:14px;line-height:27px">Lorem Ipsum is simply dummy text of the printing and typesetting industry Lorem Ipsum</p>
  <p class="abs" style="left:78px;top:266px;font-size:13px">&copy;Amber Kite Services -2019 All Rights Reserved</p>
  <h4 style="left:680px;top:38px">SITEMAP</h4>
  <ul class="footer-links"><li>Home</li><li>About</li><li>Services</li><li>Faq's</li><li>Financing</li><li>Reviews</li><li>Contact Us</li></ul>
  <h4 style="left:890px;top:38px">CONTACT US</h4>
  <svg class="abs" style="left:886px;top:86px" width="20" height="26" viewBox="0 0 20 26"><path d="M10 0a9 9 0 0 0-9 9c0 7 9 17 9 17s9-10 9-17a9 9 0 0 0-9-9z" fill="#f8c300"/><circle cx="10" cy="9" r="3.5" fill="#151515"/></svg>
  <div class="footer-contact" style="top:82px;left:922px">Amber Kite<br>101 ~ lorem ipsum simple<br>text print type industry</div>
  <svg class="abs" style="left:888px;top:178px" width="18" height="18" viewBox="0 0 24 24" fill="#f8c300"><path d="M5 3h4l2 5-2.5 1.5a11 11 0 0 0 6 6L16 13l5 2v4a2 2 0 0 1-2 2A16 16 0 0 1 3 5a2 2 0 0 1 2-2z"/></svg>
  <div class="footer-contact" style="top:172px;left:922px">123 456 7890</div>
  <svg class="abs" style="left:886px;top:206px" width="20" height="16" viewBox="0 0 20 16"><rect width="20" height="16" rx="2" fill="#f8c300"/><path d="M1 2l9 7 9-7" stroke="#151515" stroke-width="1.6" fill="none"/></svg>
  <div class="footer-contact" style="top:198px;left:922px">info@amberkite.com</div>
</footer>
<span class="social" style="left:78px"></span>
<span class="social" style="left:130px"></span>
<span class="social" style="left:182px"></span>

</body>
</html>
```